New Business Card Design Project VORASTI-Italy

we are VORASTI-Italy
our company in the market for 3 years we are luxury cosmetic company and its about time for a facelift :)
i will like to have elegant luxurious and unique business card
that will give the person that get it a unique, luxurious and elegant impression
I'm VERY OPEN FOR NEW IDEAS , even duo i add a few files of things that i see on line and i like them

i add my logo as well
my website is VORASTI.COM
(if you would like to see the main style that we have)

Target Market(s)

adult that have money :)

Industry/Entity Type

Business

Contact Information for Business Card

Name - Paul Vorasti
Position - CEO and CO Founder
address - 4817 E Larkdale
telephone - 555-384-1962
email - paul@vorasti.com
fax - 555-384-1962
website - VORASTI.COM

Colors
000000
959595
fbee3e
ffffff

Requirements
Must have
• big logo in GOLD color
• elegant look
• impressive
Nice to have
• not must but maybe classy pattern background
• not must but maybe emblem
• maybe clear plastic business card
Should not have
• colors
• images

```html
<!DOCTYPE html>
<html lang="en">
<head>
<meta charset="utf-8">
<title>VORASTI Italy – Business Card</title>
<link rel="stylesheet" href="https://fonts.googleapis.com/css2?family=Cinzel:wght@600&family=Open+Sans:wght@400&display=swap">
<style>
  :root {
    --backdrop: #2b2b2b;
    --card: #0b0b0b;
    --gold: #d9a928;
    --gold-soft: #c7982a;
    --text-light: #e6e6e6;
    --divider: #6b5520;
  }
  * { box-sizing: border-box; margin: 0; padding: 0; }
  html, body {
    width: 1200px;
    height: 900px;
    overflow: hidden;
    background: var(--backdrop);
  }
  .canvas {
    position: relative;
    width: 1200px;
    height: 900px;
    display: flex;
    align-items: center;
    justify-content: center;
    gap: 50px;
  }
  .card {
    position: relative;
    width: 520px;
    height: 300px;
    background: var(--card);
    border-radius: 22px;
    box-shadow: 0 14px 34px rgba(0,0,0,0.55);
    overflow: hidden;
  }

  /* Front: brand mark + contact */
  .card-front { display: flex; align-items: center; }
  .brand-block {
    width: 250px;
    height: 100%;
    display: flex;
    flex-direction: column;
    align-items: center;
    justify-content: center;
    gap: 18px;
  }
  .brand-circle {
    width: 120px;
    height: 120px;
    border: 3px solid var(--gold);
    border-radius: 50%;
  }
  .brand-name {
    font-family: "Cinzel", serif;
    font-weight: 600;
    font-size: 26px;
    letter-spacing: 3px;
    color: var(--gold);
  }
  .divider {
    width: 1px;
    height: 150px;
    background: linear-gradient(to bottom, transparent, var(--divider), transparent);
  }
  .contact {
    padding-left: 26px;
    color: var(--text-light);
    font-family: "Open Sans", sans-serif;
    font-size: 13px;
    line-height: 1.55;
  }
  .person-name {
    font-family: "Cinzel", serif;
    font-weight: 600;
    font-size: 19px;
    color: var(--gold);
    letter-spacing: 0.5px;
    line-height: 1.2;
  }
  .person-role { margin-bottom: 10px; }
  .contact-list { list-style: none; }
  .contact-list li { display: flex; align-items: center; gap: 8px; }
  .contact-list svg { width: 11px; height: 11px; fill: var(--gold); flex: none; }
  .address { margin-top: 10px; }

  /* Back: centred brand */
  .card-back {
    display: flex;
    flex-direction: column;
    align-items: center;
    justify-content: center;
    gap: 20px;
  }
  .back-circle {
    width: 84px;
    height: 84px;
    border: 3px solid var(--gold);
    border-radius: 50%;
  }
  .back-name {
    font-family: "Cinzel", serif;
    font-weight: 600;
    font-size: 40px;
    letter-spacing: 5px;
    color: var(--gold);
  }
</style>
</head>
<body>
<main class="canvas">
  <section class="card card-front" aria-label="Business card front">
    <div class="brand-block">
      <div class="brand-circle"></div>
      <div class="brand-name">VORASTI</div>
    </div>
    <div class="divider"></div>
    <div class="contact">
      <h1 class="person-name">PAUL VORASTI</h1>
      <p class="person-role">CEO and CO Founder</p>
      <ul class="contact-list">
        <li>
          <svg viewBox="0 0 24 24" aria-hidden="true"><path d="M6.6 10.8a15.1 15.1 0 0 0 6.6 6.6l2.2-2.2a1 1 0 0 1 1-.25 11.4 11.4 0 0 0 3.6.57 1 1 0 0 1 1 1V20a1 1 0 0 1-1 1A17 17 0 0 1 3 4a1 1 0 0 1 1-1h3.5a1 1 0 0 1 1 1c0 1.25.2 2.45.57 3.57a1 1 0 0 1-.25 1z"/></svg>
          555-384-1962
        </li>
        <li>
          <svg viewBox="0 0 24 24" aria-hidden="true"><path d="M7 2h10v5H7zM4 8h16a2 2 0 0 1 2 2v7h-4v5H6v-5H2v-7a2 2 0 0 1 2-2zm4 8v4h8v-4z"/></svg>
          555-384-1962
        </li>
        <li>
          <svg viewBox="0 0 24 24" aria-hidden="true"><path d="M2 5h20v14H2zm2 2v.5l8 5 8-5V7l-8 5z"/></svg>
          paul@vorasti.com
        </li>
        <li>
          <svg viewBox="0 0 24 24" aria-hidden="true"><circle cx="12" cy="12" r="10"/></svg>
          www.vorasti.com
        </li>
      </ul>
      <p class="address">4817 E Larkdale</p>
    </div>
  </section>

  <section class="card card-back" aria-label="Business card back">
    <div class="back-circle"></div>
    <div class="back-name">VORASTI ITALY</div>
  </section>
</main>
</body>
</html>
```